Industrial Project Sign

We need an eye catching (but professional) industrial project sign that will be very large (roughly 12' high x 18' wide). This sign will be highly visible from the adjacent high speed highway.

* The following needs to be at the bottom of the signage: Logo (uploaded), Name (Halvern Land Holdings, Inc.) (uploaded) and phone number (555)739-2864

*Name of Project - "Marrowfield Logistics Park"

* Text items
Land for Sale
Build to Suit
Zoning: Industrial (G I & L I)

* Interesting background that is eye catching

Good morning all,

We are considering all designers options as we go and are waiting for the final designs to come in by the 4th so that we can give each one a good look.   If you have any new designs, questions, further design options or any tweeks you want to do to current designs, please do so at this time.

Thanks to all of you for your submissions.

Industrial

```html
<!DOCTYPE html>
<html lang="en">
<head>
<meta charset="utf-8">
<title>Marrowfield Logistics Park – Project Sign</title>
<link rel="stylesheet" href="https://fonts.googleapis.com/css2?family=PT+Sans:wght@400;700&display=swap">
<style>
  :root {
    --maroon: #600000;
    --white: #ffffff;
    --ink: #3a3a3a;
    --ink-dark: #1a1a1a;
    --badge: #7fdcef;
  }
  html, body {
    margin: 0;
    padding: 0;
    width: 1200px;
    height: 798px;
    overflow: hidden;
    background: var(--white);
  }
  .sign {
    position: relative;
    width: 1200px;
    height: 798px;
    box-sizing: border-box;
    background: var(--maroon);
    border-radius: 40px;
    padding: 28px 30px;
    font-family: "PT Sans", sans-serif;
  }
  .sign__face {
    position: relative;
    width: 100%;
    height: 100%;
    background: var(--white);
    border-radius: 22px;
  }
  .developer {
    position: absolute;
    left: 420px;
    top: 90px;
    width: 470px;
  }
  .developer__name {
    margin: 0;
    font-size: 30px;
    font-weight: 700;
    color: var(--ink);
    letter-spacing: 0.2px;
    padding-left: 32px;
    display: flex;
    align-items: center;
    gap: 14px;
  }
  .developer__mark {
    width: 18px;
    height: 18px;
    background: var(--maroon);
    flex: none;
  }
  .developer__rule {
    height: 4px;
    background: var(--maroon);
    margin-top: 8px;
    margin-left: 25px;
  }
  .project {
    position: absolute;
    left: 2px;
    right: 2px;
    top: 224px;
    height: 398px;
    background: var(--maroon);
    border-radius: 22px;
    color: var(--white);
  }
  .project__title {
    margin: 0;
    padding-top: 22px;
    text-align: center;
    font-size: 68px;
    font-weight: 700;
    line-height: 1.1;
  }
  .project__features {
    list-style: none;
    margin: 26px 0 0 178px;
    padding: 0;
    font-size: 58px;
    line-height: 80px;
  }
  .contact {
    position: absolute;
    left: 76px;
    top: 650px;
    display: flex;
    align-items: center;
    gap: 26px;
  }
  .contact__badge {
    width: 74px;
    height: 74px;
    border-radius: 50%;
    background: var(--badge);
  }
  .contact__phone {
    font-size: 64px;
    font-weight: 700;
    color: var(--maroon);
    letter-spacing: 1px;
  }
  .brand-tag {
    position: absolute;
    right: 90px;
    bottom: 14px;
    font-size: 20px;
    font-weight: 700;
    color: var(--ink-dark);
  }
</style>
</head>
<body>
  <div class="sign">
    <div class="sign__face">
      <header class="developer">
        <p class="developer__name"><span class="developer__mark"></span>Halvern Land Holdings, Inc.</p>
        <div class="developer__rule"></div>
      </header>

      <section class="project">
        <h1 class="project__title">Marrowfield Logistics Park</h1>
        <ul class="project__features">
          <li>Land for Sale</li>
          <li>Build to Suit</li>
          <li>Zoning: Industrial (G I &amp; L I)</li>
        </ul>
      </section>

      <footer class="contact">
        <span class="contact__badge" aria-hidden="true"></span>
        <span class="contact__phone">(555) 739-2864</span>
      </footer>
      <span class="brand-tag">HALVERN</span>
    </div>
  </div>
</body>
</html>
```